Business card needed for the Vantro of Dry Cleaning!

We need a slick business card design for a new company based out of Montreal called Casiers Pli&Zip inc. (in French) and Pli&Zip Lockers inc. (in English). We're the Vantro of Laundry. We offer services of dry cleaning, laundry (wash&fold), minor clothing alterations, shoe repair and parcel delivery through 24/7 secured and connected lockers. Ordres are placed through our mobile application. Real time notification are sent to customers when their order is ready for pickup. The lockers will be placed throughout the downtown area, in condo and office towers, where a high density of busy people converge. It is simple, user-friendly, and most importantly convenient. We're the out of the box dry cleaner, literally.
Updates

Target Market(s)

1) Professional workers wearing suits daily
2) Campus students living in residences
3) People using laundromats
4) Families with children/yuppies who prefer to use their time doing something else than laundry

Industry/Entity Type

Dry Cleaning

Contact Information for Business Card

Name / Sylvie-Anne Berthiaume
Title / CEO & Founder
Company Name / Casiers Pli&Zip inc. | Pli&Zip Lockers inc.
Website www.plizip.ca

Requirements
Must have
• Text Logo: Pli&Zip - Nettoyeurs 24/7 Cleaners
• Logo on one side and contact info on the other (bilingual)
• Minimalist, pure design
• "We care" for your belongings feeling
• Professional, technological, clean & fresh look
Should not have
• No busy visuals. No rainbow colors.

```html
<!DOCTYPE html>
<html lang="fr">
<head>
<meta charset="utf-8">
<title>Pli&amp;Zip – Cartes d'affaires</title>
<link rel="stylesheet" href="https://fonts.googleapis.com/css2?family=Mulish:wght@400;700&display=swap">
<style>
  :root {
    --backdrop: #1c1c1c;
    --card: #f3f3f3;
    --ink-grey: #666666;
    --ink-dark: #333333;
    --brand-blue: #0a7fd1;
    --rule: #d6d6d6;
  }
  * { margin: 0; padding: 0; box-sizing: border-box; }
  html, body {
    width: 1200px;
    height: 1001px;
    overflow: hidden;
    background: var(--backdrop);
  }
  .canvas { position: relative; width: 1200px; height: 1001px; }
  .card {
    position: absolute;
    left: 306px;
    width: 589px;
    height: 329px;
    background: var(--card);
  }
  .card--front { top: 133px; }
  .card--back { top: 539px; }

  .brand-name {
    font-family: "Mulish", sans-serif;
    font-weight: 700;
    color: var(--ink-dark);
    line-height: 1;
    white-space: nowrap;
  }
  .brand-sub {
    font-family: "Mulish", sans-serif;
    font-weight: 400;
    color: var(--ink-grey);
    line-height: 1;
    letter-spacing: 1px;
    white-space: nowrap;
  }

  /* Front: name block + contact */
  .front-brand {
    position: absolute;
    right: 321px;
    top: 136px;
    display: flex;
    flex-direction: column;
    align-items: flex-end;
    gap: 10px;
  }
  .front-brand .brand-name { font-size: 34px; }
  .front-brand .brand-sub { font-size: 13px; }

  .divider {
    position: absolute;
    left: 294px;
    top: 91px;
    width: 1px;
    height: 146px;
    background: var(--rule);
  }
  .contact {
    position: absolute;
    left: 320px;
    top: 110px;
    font-family: "Mulish", sans-serif;
    color: var(--ink-dark);
  }
  .contact__name {
    font-weight: 700;
    font-size: 16px;
    letter-spacing: 0.3px;
    color: var(--brand-blue);
    text-transform: uppercase;
    line-height: 1.2;
  }
  .contact__title { font-size: 14.5px; line-height: 1.3; margin-bottom: 15px; }
  .contact__line { font-size: 14.5px; line-height: 19px; }
  .contact__label { font-weight: 700; color: var(--brand-blue); }

  /* Back: centred name */
  .back-brand {
    position: absolute;
    left: 0;
    right: 0;
    top: 130px;
    display: flex;
    flex-direction: column;
    align-items: center;
    gap: 14px;
  }
  .back-brand .brand-name { font-size: 46px; }
  .back-brand .brand-sub { font-size: 17px; }
  .back-url {
    position: absolute;
    left: 0;
    right: 0;
    top: 277px;
    text-align: center;
    font-family: "Mulish", sans-serif;
    font-size: 16px;
    letter-spacing: 0.5px;
    color: var(--ink-grey);
  }
</style>
</head>
<body>
<main class="canvas">
  <section class="card card--front" aria-label="Recto de la carte">
    <div class="front-brand">
      <div class="brand-name">Pli&amp;Zip</div>
      <div class="brand-sub">Casiers / Lockers</div>
    </div>
    <div class="divider"></div>
    <div class="contact">
      <p class="contact__name">Sylvie-Anne Berthiaume</p>
      <p class="contact__title">CEO &amp; Founder</p>
      <p class="contact__line"><span class="contact__label">T:</span> 514-555-0182</p>
      <p class="contact__line"><span class="contact__label">E:</span> info@plizip.ca</p>
      <p class="contact__line"><span class="contact__label">W:</span> www.plizip.ca</p>
    </div>
  </section>

  <section class="card card--back" aria-label="Verso de la carte">
    <div class="back-brand">
      <div class="brand-name">Pli&amp;Zip</div>
      <div class="brand-sub">Casiers / Lockers</div>
    </div>
    <p class="back-url">www.plizip.ca</p>
  </section>
</main>
</body>
</html>
```